High profile consultancy

We need a web design for a company called BK Services. BK as abbreviation for Bold Keystone.

Company focusses on Sourcing (BK Sourcing, focus on ICT), Metrics (BK Metrics; focus on business case analysis and trends in ICT) and Software (BK software; to be developed later on; mainly tools supporting BK soucing and metrics)

Customers base consists of large enterprises, >1000 employees.

Site needs to have menu's for
- services
- login
- about
and a special area ' inspire ' to be able to communicate topics that should inspire our customers to contact us.

but key; it schould communicate our expertise and focus on deep knowlegde of ICT sourcing

Reason: please advice on content management systems to be used to maintain site also please advice on Trovix search clickbids. Will provide feedback on designs shortly.

Target Market(s)

CIO's; board of directors;
company excels in ICT / business knowledge and ability to execute; creates / optimizes relations between ICT suppliers and enterprises.

Requirements
Must have
• website should be easily be found; adaptive by design; accessible by all browsers.
• Need to have a login section for later use
Nice to have
• usage of (draft) logo. see upload.

```html
<!DOCTYPE html>
<html lang="en">
<head>
<meta charset="utf-8">
<title>BK Services – ICT Strategy Consulting and Execution</title>
<link rel="stylesheet" href="https://fonts.googleapis.com/css2?family=Roboto+Condensed:wght@400;700&family=Roboto:wght@400;500&display=swap">
<style>
:root{
  --blue:#1b6fb5;
  --blue-dark:#0f5a9c;
  --navy:#1d3f7a;
  --text:#333;
  --muted:#8a8a8a;
  --input:#ececec;
  --card-border:#dcdcdc;
  --icon-bg:#ebebd9;
  --icon:#6b6b6b;
  --date-bg:#d6d3c9;
  --footer:#4b4b4b;
  --footer-text:#f2f2f2;
  --orange:#f0a020;
}
*{box-sizing:border-box;margin:0;padding:0}
html,body{width:1200px;height:1029px;overflow:hidden;background:#fff}
body{position:relative;font-family:"Roboto Condensed",Arial,sans-serif;color:var(--text)}
a{color:inherit;text-decoration:none}
.abs{position:absolute}

/* header */
.brand{left:121px;top:30px;display:flex;align-items:center;gap:10px;color:var(--navy);font-size:26px;font-weight:400;white-space:nowrap}
.brand-mark{width:34px;height:34px;border-radius:50%;background:var(--blue)}
.main-nav{left:350px;top:33px;height:29px;display:flex;align-items:center;font-size:10px;text-transform:uppercase;color:#444}
.main-nav a{display:block}
.nav-home{width:65px;height:29px;line-height:29px;text-align:center;color:#fff;background:linear-gradient(#2f8ee0,#1769b8);border-radius:2px}
.nav-item{position:absolute;top:9px;white-space:nowrap}
.nav-sep{position:absolute;top:8px;color:#777}

.login{left:870px;top:10px;width:210px;font-size:10px;color:#555}
.login-title{position:absolute;left:54px;top:0;font-weight:700;color:#222;white-space:nowrap}
.login-label{position:absolute;left:-16px;width:64px;text-align:right;color:#777;white-space:nowrap}
.login-field{position:absolute;left:54px;width:155px;height:16px;background:var(--input);border:none}
.btn-login{position:absolute;left:54px;top:62px;width:47px;height:16px;line-height:16px;text-align:center;color:#fff;background:var(--blue);border-radius:2px}
.btn-register{position:absolute;left:111px;top:62px;width:46px;height:16px;line-height:16px;text-align:center;color:#222;background:#e4e4e4;border-radius:2px}
.forgot{position:absolute;left:54px;top:84px;color:#222;white-space:nowrap}
.forgot span{color:#aaa;margin-left:4px}

/* hero */
.hero-floor{left:0;top:340px;width:1200px;height:150px;background:linear-gradient(180deg,#fff 0%,#ececec 45%,#e2e2e2 70%,#f4f4f4 100%)}
.hero-title{left:119px;top:158px;font-size:19px;font-weight:700;color:var(--blue);white-space:nowrap}
.hero-lead{left:121px;top:194px;width:428px;font-size:11.5px;line-height:17px;color:#555}
.hero-lead b{font-size:19px;font-weight:400;color:var(--blue)}
.hero-network{left:168px;top:263px;width:278px;height:177px;border-radius:50% 50% 10px 10px;background:radial-gradient(ellipse at 50% 30%,#cfcfcf 0%,#e8e8e8 45%,rgba(255,255,255,0) 72%)}
.hero-team{left:610px;top:197px;width:473px;height:243px;background:linear-gradient(180deg,#d9d2cc 0%,#3a3b40 35%,#2b2c30 70%,#8c8c8c 100%);border-radius:60px 60px 4px 4px}

/* services */
.service{top:457px;width:179px;height:249px;background:#fff;border:1px solid var(--card-border);border-top:3px solid #cfcfcf;box-shadow:0 2px 4px rgba(0,0,0,.12)}
.service h3{margin-top:22px;text-align:center;font-family:"Roboto",Arial,sans-serif;font-weight:500;font-size:11.5px;color:#222}
.service-icon{width:59px;height:55px;margin:16px auto 0;background:var(--icon-bg);display:flex;align-items:center;justify-content:center}
.service p{margin:40px 14px 0;font-size:10px;line-height:15px;color:#888;text-align:center}
.btn-more{display:block;width:53px;height:18px;line-height:18px;margin:26px auto 0;text-align:center;font-size:10px;color:#fff;background:var(--blue-dark);border-radius:2px}

/* about & news */
.section-title{top:746px;font-size:11.5px;font-weight:400;text-transform:uppercase;color:#333}
.about-video{left:119px;top:771px;width:179px;height:129px;background:linear-gradient(135deg,#cfc3b6 0%,#a8998c 45%,#2d2d33 100%)}
.about-video svg{position:absolute;left:78px;top:50px}
.about-text{left:315px;top:767px;width:292px;font-size:10px;line-height:15.2px;color:#888}
.btn-grey{left:315px;top:880px;width:54px;height:18px;line-height:18px;text-align:center;font-size:10px;color:#222;background:#ddd;border-radius:2px}
.news-item{left:705px;width:380px;height:50px}
.news-date{position:absolute;left:0;top:0;width:54px;height:49px;background:var(--date-bg);text-align:center;color:#222}
.news-date strong{display:block;font-size:24px;line-height:28px;margin-top:2px}
.news-date span{display:block;font-size:10px}
.news-body{position:absolute;left:85px;top:0;width:295px}
.news-body h4{font-size:11px;font-weight:400;color:#1d3f7a;margin-top:-1px}
.news-body p{font-size:10px;line-height:15.5px;color:#888;margin-top:5px;white-space:nowrap}

/* footer */
.site-footer{left:0;top:944px;width:1200px;height:85px;background:var(--footer);color:var(--footer-text);font-size:10px}
.footer-nav{position:absolute;left:119px;top:12px;text-transform:uppercase}
.footer-nav a,.footer-nav i{position:absolute;white-space:nowrap;font-style:normal}
.footer-nav .current{color:var(--orange)}
.copyright{position:absolute;right:121px;top:10px;white-space:nowrap}
.follow{position:absolute;left:119px;top:48px;display:flex;align-items:center;gap:8px;font-size:11px;white-space:nowrap}
.social{display:flex;align-items:center;gap:4px;padding:0 6px;height:24px;border-radius:3px;background:#5a5a5a;font-size:10px}
.social::before{content:"";width:8px;height:8px;background:#9a9a9a}
</style>
</head>
<body>

<header>
  <a class="abs brand" href="#"><span class="brand-mark"></span>BK Services</a>

  <nav class="abs main-nav" aria-label="Main">
    <a class="nav-home" href="#">HOME</a>
    <a class="nav-item" style="left:99px" href="#">About us</a>
    <span class="nav-sep" style="left:162px">|</span>
    <a class="nav-item" style="left:186px" href="#">Services</a>
    <span class="nav-sep" style="left:247px">|</span>
    <a class="nav-item" style="left:270px" href="#">Clients</a>
    <span class="nav-sep" style="left:326px">|</span>
    <a class="nav-item" style="left:346px" href="#">News</a>
    <span class="nav-sep" style="left:389px">|</span>
    <a class="nav-item" style="left:414px" href="#">Contact us</a>
  </nav>

  <form class="abs login" aria-label="Member login">
    <div class="login-title">Member Log - in</div>
    <label class="login-label" style="top:22px">User Name :</label>
    <input class="login-field" style="top:20px" type="text" aria-label="User name">
    <label class="login-label" style="top:43px">Password :</label>
    <input class="login-field" style="top:41px" type="password" aria-label="Password">
    <a class="btn-login" href="#">Login</a>
    <a class="btn-register" href="#">Register</a>
    <div class="forgot">Forget Password..? <span>Click Here</span></div>
  </form>
</header>

<section>
  <div class="abs hero-floor" role="img" aria-label="Light grey perspective tiled floor"></div>
  <h1 class="abs hero-title">ICT Strategy Consulting and Execution</h1>
  <p class="abs hero-lead"><b>BK</b> provides enterprise level consulting in Information and Communication Technology systems and their implications on your business</p>
  <div class="abs hero-network" role="img" aria-label="Globe illustration surrounded by connected laptops"></div>
  <div class="abs hero-team" role="img" aria-label="Photo of a large team of business people in suits"></div>
</section>

<section aria-label="Services">
  <article class="abs service" style="left:119px">
    <h3>Technical consultant</h3>
    <div class="service-icon"><svg width="28" height="28" viewBox="0 0 28 28" fill="var(--icon)"><circle cx="14" cy="11" r="6"/><path d="M4 27c0-6 4-9 10-9s10 3 10 9z"/><path d="M7 11a7 7 0 0 1 14 0" fill="none" stroke="var(--icon)" stroke-width="2"/></svg></div>
    <p>Lorem Ipsum is simply dummy text of the printing and typesetting industry. Lorem Ipsum has been the industry's</p>
    <a class="btn-more" href="#">Read more</a>
  </article>
  <article class="abs service" style="left:315px">
    <h3>Business execution</h3>
    <div class="service-icon"><svg width="28" height="28" viewBox="0 0 28 28" fill="var(--icon)"><circle cx="12" cy="10" r="5"/><path d="M3 27c0-6 4-9 9-9s9 3 9 9z"/><path d="M21 5a6 6 0 0 1 0 8M24 3a9 9 0 0 1 0 12" fill="none" stroke="var(--icon)" stroke-width="1.6"/></svg></div>
    <p>Lorem Ipsum is simply dummy text of the printing and typesetting industry. Lorem Ipsum has been the industry's</p>
    <a class="btn-more" href="#">Read more</a>
  </article>
  <article class="abs service" style="left:510px">
    <h3>Business case analysis</h3>
    <div class="service-icon"><svg width="26" height="28" viewBox="0 0 26 28"><rect x="3" y="3" width="20" height="24" rx="2" fill="var(--icon)"/><rect x="8" y="1" width="10" height="5" rx="1" fill="#444"/><path d="M7 11h12M7 15h12M7 19h12M7 23h8" stroke="#ebebd9" stroke-width="1.5"/></svg></div>
    <p>Lorem Ipsum is simply dummy text of the printing and typesetting industry. Lorem Ipsum has been the industry's</p>
    <a class="btn-more" href="#">Read more</a>
  </article>
  <article class="abs service" style="left:706px">
    <h3>Process Optimization</h3>
    <div class="service-icon"><svg width="22" height="28" viewBox="0 0 22 28" fill="var(--icon)"><rect x="1" y="1" width="20" height="3"/><rect x="1" y="24" width="20" height="3"/><path d="M4 4h14c0 6-5 8-5 10s5 4 5 10H4c0-6 5-8 5-10S4 10 4 4z"/></svg></div>
    <p>Lorem Ipsum is simply dummy text of the printing and typesetting industry. Lorem Ipsum has been the industry's</p>
    <a class="btn-more" href="#">Read more</a>
  </article>
  <article class="abs service" style="left:901px">
    <h3>Competitive Analysis</h3>
    <div class="service-icon"><svg width="24" height="28" viewBox="0 0 24 28"><rect x="1" y="1" width="22" height="26" rx="2" fill="var(--icon)"/><rect x="4" y="4" width="16" height="6" fill="#ebebd9"/><g fill="#ebebd9"><rect x="4" y="13" width="4" height="3"/><rect x="10" y="13" width="4" height="3"/><rect x="16" y="13" width="4" height="3"/><rect x="4" y="18" width="4" height="3"/><rect x="10" y="18" width="4" height="3"/><rect x="16" y="18" width="4" height="3"/><rect x="4" y="23" width="4" height="2"/><rect x="10" y="23" width="4" height="2"/><rect x="16" y="23" width="4" height="2"/></g></svg></div>
    <p>Lorem Ipsum is simply dummy text of the printing and typesetting industry. Lorem Ipsum has been the industry's</p>
    <a class="btn-more" href="#">Read more</a>
  </article>
</section>

<section aria-label="About us">
  <h2 class="abs section-title" style="left:119px">About us</h2>
  <div class="abs about-video" role="img" aria-label="Video still of a young businessman adjusting his glasses">
    <svg width="24" height="22" viewBox="0 0 24 22"><rect width="24" height="22" rx="3" fill="#d62020"/><path d="M9 6l7 5-7 5z" fill="#fff"/></svg>
  </div>
  <p class="abs about-text">Lorem Ipsum is simply dummy text of the printing and typesetting indus-try. Lorem Ipsum has been the industry's standard dummy text ever since the 1500s, when an unknown printer took a galley of type and scrambled it to make a type specimen book. It has survived not only five centuries, but also the leap into electronic typesetting, remaining essentially unchanged. It was popularised in the 1960s with the release of Kerntype sheets containing Lorem Ipsum passages, and more recently with desk-</p>
  <a class="abs btn-grey" href="#">Read more</a>
</section>

<section aria-label="Latest news">
  <h2 class="abs section-title" style="left:705px">Latest news</h2>
  <article class="abs news-item" style="top:771px">
    <div class="news-date"><strong>22</strong><span>Nov 2013</span></div>
    <div class="news-body"><h4>News Headline Goes Here</h4><p>Lorem Ipsum is simply dummy text of the printing and typesetting indus-<br>try. Lorem Ipsum has been the industry's standard dummy text ever since</p></div>
  </article>
  <article class="abs news-item" style="top:838px">
    <div class="news-date"><strong>22</strong><span>Nov 2013</span></div>
    <div class="news-body"><h4>News Headline Goes Here</h4><p>Lorem Ipsum is simply dummy text of the printing and typesetting indus-<br>try. Lorem Ipsum has been the industry's standard dummy text ever since</p></div>
  </article>
</section>

<footer class="abs site-footer">
  <nav class="footer-nav" aria-label="Footer">
    <a class="current" style="left:0" href="#">Home</a>
    <i style="left:54px">|</i>
    <a style="left:72px" href="#">About us</a>
    <i style="left:134px">|</i>
    <a style="left:158px" href="#">Services</a>
    <i style="left:220px">|</i>
    <a style="left:245px" href="#">Clients</a>
    <i style="left:299px">|</i>
    <a style="left:322px" href="#">News</a>
    <i style="left:366px">|</i>
    <a style="left:389px" href="#">Contact us</a>
  </nav>
  <div class="copyright">All copyright 2013 reserved by Northfield Design</div>
  <div class="follow">FOLLOW US :
    <a class="social" href="#">Friendwall</a>
    <a class="social" href="#">Vidstream</a>
    <a class="social" href="#">Feed</a>
    <a class="social" href="#">Chirper</a>
  </div>
</footer>

</body>
</html>
```